Clothing Brand E-Commerce Website Design

We would like you to provide an ecommerce design template in layered PSD for our clothing/fashion brand website called "FernQuill".
We want the site to have a simple but sleek design similar to the following sites:
http://www.threadorbit.example/
http://tovalenwick.example/
http://www.sadiplume.example/
We want it to look stunning and blow the example sites out of the water. For color scheme, please use your imagination and try to impress us with your creativity.
We like teal and beige pink, with teal dominant.
Teal #7AFFFF / #46C6C6
Beige/pink #FF7B7C / #C74646
We want you to develop the design for 3 pages:
1) Home Page
Samples:
http://www.threadorbit.example/
http://tovalenwick.example/
http://www.sadiplume.example/
2) Products List Page (e.g., lists all "Dresses" when category is selected)
http://www.threadorbit.example/shop/casual-dresses
http://www.sadiplume.example/index.php?main_page=index&cPath=3
http://tovalenwick.example/modest-dresses.html
http://www.lunahive88.example/Product/Category.aspx?br=lh8&category=dress_maxi
3) Product Detail Page (e.g., individual product page with "Add to Cart")
http://www.threadorbit.example/shop/dresses/willow-dawn-dress
http://tovalenwick.example/modest-dresses/modest-dress-opal.html
http://www.sadiplume.example/index.php?main_page=product_info&cPath=3&products_id=297
Industry/Entity Type
Fashion

```html
<!DOCTYPE html>
<html lang="en">
<head>
<meta charset="utf-8">
<title>FernQuill — Home</title>
<link href="https://fonts.googleapis.com/css2?family=PT+Sans+Narrow:wght@400;700&family=Parisienne&display=swap" rel="stylesheet">
<style>
  :root {
    --teal: #7affff;
    --teal-deep: #46c6c6;
    --coral: #ff7b7c;
    --coral-deep: #c74646;
    --ink: #3a3a3a;
    --text: #5a5a5a;
    --muted: #8a8a8a;
    --rule: #dcdcdc;
    --tile: #f2f2f2;
    --paper: #ffffff;
  }
  * { box-sizing: border-box; margin: 0; padding: 0; }
  html, body { width: 849px; height: 1200px; overflow: hidden; background: var(--paper); }
  body { font-family: "PT Sans Narrow", "Arial Narrow", sans-serif; color: var(--text); position: relative; }
  .abs { position: absolute; }

  /* header */
  .support { left: 188px; top: 31px; font-size: 9px; color: var(--text); }
  .support-mark { left: 237px; top: 46px; width: 40px; height: 2px; background: var(--teal-deep); }
  .brand { left: 325px; top: 10px; width: 200px; text-align: center; font-size: 22px; color: var(--ink); letter-spacing: .5px; }
  .account { left: 542px; top: 31px; font-size: 9px; display: flex; gap: 10px; }
  .header-rule { left: 183px; top: 47px; width: 484px; height: 1px; background: var(--rule); }
  .nav { left: 114px; top: 60px; width: 622px; display: flex; justify-content: center; gap: 21px; font-size: 10px; color: var(--text); }
  .nav-rule { left: 114px; top: 84px; width: 622px; height: 2px; background: var(--teal); }

  /* hero */
  .hero { left: 114px; top: 97px; width: 622px; height: 234px;
    background: radial-gradient(ellipse 45% 70% at 48% 45%, #ffffff 0%, #c9ffff 35%, var(--teal) 85%); overflow: hidden; }
  .hero-title { left: 112px; top: 60px; font-family: "Parisienne", cursive; font-size: 44px; color: var(--coral); white-space: nowrap; }
  .hero-copy { left: 125px; top: 116px; width: 170px; text-align: center; font-size: 8.5px; line-height: 12px; color: var(--text); }
  .hero-btn { left: 151px; top: 149px; width: 107px; height: 19px; border: 1px solid var(--coral); color: var(--coral); font-size: 8.5px; text-align: center; line-height: 17px; }
  .hero-photo { left: 392px; top: 0; width: 102px; height: 234px;
    background: linear-gradient(180deg, #cfcfcf 0%, #6e6e6e 35%, #9a9a9a 55%, #2a2a2a 80%, #1a1a1a 100%); border-radius: 40px 40px 0 0; }
  .dots { left: 293px; top: 218px; display: flex; gap: 4px; }
  .dots span { width: 7px; height: 7px; border-radius: 50%; background: #cfcfcf; }
  .dots span.on { background: var(--coral); }
  .hero-shadow { left: 170px; top: 331px; width: 520px; height: 20px;
    background: radial-gradient(ellipse 50% 100% at 50% 0%, rgba(0,0,0,.28), rgba(0,0,0,0) 70%); }

  /* section heads */
  .sec-rule-top { left: 114px; width: 622px; height: 2px; background: var(--rule); }
  .sec-rule-bot { left: 114px; width: 622px; height: 1px; background: var(--teal); }
  .sec-title { left: 114px; width: 622px; text-align: center; font-size: 12px; color: var(--text); }

  /* product cards */
  .card { width: 146px; border: 1px solid #ececec; background: var(--paper); }
  .card-photo { width: 100%; background: linear-gradient(180deg, var(--tile), #e6e6e6); }
  .card-name { text-align: center; font-size: 11px; color: var(--text); margin-top: 10px; }
  .card-price { text-align: center; font-size: 13px; color: var(--ink); margin-top: 3px; }
  .cart-btn { width: 61px; height: 22px; border: 1px solid var(--coral); color: var(--coral); font-size: 8.5px; text-align: center; line-height: 20px; background: var(--paper); }
  .promo { left: 117px; top: 752px; width: 142px; height: 147px; background: #333333; }
  .promo-tag { left: 44px; top: 8px; width: 54px; height: 132px; border-radius: 24px 24px 6px 6px;
    background: linear-gradient(180deg, #a7c63a, #8fb12a); }

  /* footer */
  .footer-rule { left: 114px; top: 1000px; width: 622px; height: 2px; background: var(--rule); }
  .foot-col { font-size: 8.5px; color: var(--text); line-height: 22px; }
  .social { left: 592px; top: 1017px; display: flex; gap: 3px; }
  .social span { width: 14px; height: 14px; border-radius: 2px; }
  .subscribe { left: 592px; top: 1048px; font-size: 8.5px; }
  .email { left: 592px; top: 1067px; width: 144px; height: 18px; border: 1px solid var(--rule); font-size: 8px; color: var(--muted); padding-left: 8px; line-height: 16px; }
  .submit { left: 592px; top: 1091px; width: 90px; height: 18px; border: 1px solid var(--coral); color: var(--coral); font-size: 8.5px; text-align: center; line-height: 16px; }
  .bottom-rule { left: 114px; top: 1141px; width: 622px; height: 1px; background: #ececec; }
  .copyright { left: 114px; top: 1151px; width: 650px; text-align: center; font-size: 8px; color: var(--muted); }
</style>
</head>
<body>

<header>
  <div class="abs support">Support: +880-1700-418260</div>
  <div class="abs support-mark"></div>
  <div class="abs brand">FernQuill</div>
  <div class="abs account"><span>Sign In</span><span>|</span><span>Cart (0)</span><span>|</span><span>Register</span></div>
  <div class="abs header-rule"></div>
  <nav class="abs nav">
    <span>Home</span><span>New!</span><span>Tops</span><span>Bottoms</span><span>Dresses</span><span>Accessories</span><span>Clearance</span><span>Blog</span><span>Contact</span>
  </nav>
  <div class="abs nav-rule"></div>
</header>

<section class="abs hero">
  <div class="abs hero-title">June Special</div>
  <p class="abs hero-copy">Lorem Ipsum dolor sit amet this is just a dummy text needs to be replaced with original texts</p>
  <div class="abs hero-btn">Start Shopping</div>
  <div class="abs hero-photo" role="img" aria-label="Model in a black leather jacket and skirt, black and white photo"></div>
  <div class="abs dots"><span class="on"></span><span></span><span></span><span></span></div>
</section>
<div class="abs hero-shadow"></div>

<!-- New Arrivals -->
<div class="abs sec-rule-top" style="top:366px"></div>
<h2 class="abs sec-title" style="top:378px;font-weight:400">New Arrivals</h2>
<div class="abs sec-rule-bot" style="top:403px"></div>

<div class="abs card" style="left:114px;top:424px;height:226px">
  <div class="card-photo" style="height:165px" role="img" aria-label="Model in black top, grey skirt and boots"></div>
  <div class="card-name">Womens Outfit</div><div class="card-price">$100</div>
</div>
<div class="abs card" style="left:272px;top:424px;height:226px">
  <div class="card-photo" style="height:165px" role="img" aria-label="Model in black top, grey skirt and boots"></div>
  <div class="card-name">Womens Outfit</div><div class="card-price">$100</div>
</div>
<div class="abs card" style="left:430px;top:424px;height:226px">
  <div class="card-photo" style="height:165px" role="img" aria-label="Model in black top, grey skirt and boots"></div>
  <div class="card-name">Womens Outfit</div><div class="card-price">$100</div>
</div>
<div class="abs card" style="left:589px;top:424px;height:226px">
  <div class="card-photo" style="height:165px" role="img" aria-label="Model in black top, grey skirt and boots"></div>
  <div class="card-name">Womens Outfit</div><div class="card-price">$100</div>
</div>
<div class="abs cart-btn" style="left:156px;top:639px">Add to Cart</div>
<div class="abs cart-btn" style="left:314px;top:639px">Add to Cart</div>
<div class="abs cart-btn" style="left:473px;top:639px">Add to Cart</div>
<div class="abs cart-btn" style="left:632px;top:639px">Add to Cart</div>

<!-- Popular Items -->
<div class="abs sec-rule-top" style="top:695px"></div>
<h2 class="abs sec-title" style="top:707px;font-weight:400">Popular Items</h2>
<div class="abs sec-rule-bot" style="top:732px"></div>

<div class="abs promo">
  <div class="abs promo-tag" role="img" aria-label="Green door-hanger tag reading special offer, 70 percent discount"></div>
</div>
<div class="abs card" style="left:272px;top:752px;height:208px">
  <div class="card-photo" style="height:147px" role="img" aria-label="Model in black blazer over white top"></div>
  <div class="card-name">Womens Outfit</div><div class="card-price">$100</div>
</div>
<div class="abs card" style="left:430px;top:752px;height:208px">
  <div class="card-photo" style="height:147px" role="img" aria-label="Model in black blazer over white top"></div>
  <div class="card-name">Womens Outfit</div><div class="card-price">$100</div>
</div>
<div class="abs card" style="left:589px;top:752px;height:208px">
  <div class="card-photo" style="height:147px" role="img" aria-label="Model in black blazer over white top"></div>
  <div class="card-name">Womens Outfit</div><div class="card-price">$100</div>
</div>
<div class="abs cart-btn" style="left:314px;top:948px">Add to Cart</div>
<div class="abs cart-btn" style="left:473px;top:948px">Add to Cart</div>
<div class="abs cart-btn" style="left:632px;top:948px">Add to Cart</div>

<footer>
  <div class="abs footer-rule"></div>
  <div class="abs foot-col" style="left:125px;top:1013px">About Company<br>Careers<br>Testimonials<br>Press</div>
  <div class="abs foot-col" style="left:283px;top:1013px">New Arrivals<br>Clothing<br>Shoes<br>Bags &amp; Accessories<br>Apartment</div>
  <div class="abs foot-col" style="left:434px;top:1013px">Customers<br>Suppport<br>Contact Us<br>Live Chat</div>
  <div class="abs social" aria-label="Social links">
    <span style="background:#3b5998"></span><span style="background:#2fa5e0"></span><span style="background:#cb2027"></span><span style="background:#0e76a8"></span><span style="background:#e62d2d"></span>
  </div>
  <div class="abs subscribe">Subscribe</div>
  <div class="abs email">Email</div>
  <div class="abs submit">Submit</div>
  <div class="abs bottom-rule"></div>
  <div class="abs copyright">Copyright @ Lorem Ipsum. All rights Reserved</div>
</footer>

</body>
</html>
```